Drone company needs a brochure design

We would like a brochure design which compliments our existing logo, website and business card designs.

www.tallowmerrin.com.au

Business

```html
<!DOCTYPE html>
<html lang="en">
<head>
<meta charset="utf-8">
<title>Tallow Merrin – Corporate Business Brochure</title>
<link rel="stylesheet" href="https://fonts.googleapis.com/css2?family=Fira+Sans:wght@300;400;500;600&display=swap">
<style>
  :root {
    --paper: #ffffff;
    --grey-heading: #8e9194;
    --grey-light: #a3a6a9;
    --brand-blue: #0a86c4;
    --brand-blue-deep: #0479b5;
    --brand-cyan: #2ba9e1;
    --ink: #1c1e21;
    --white: #ffffff;
  }
  * { margin: 0; padding: 0; box-sizing: border-box; }
  html, body { width: 1200px; height: 1200px; overflow: hidden; background: var(--paper); }
  body { position: relative; font-family: "Fira Sans", sans-serif; }

  .tagline { position: absolute; left: 198px; top: 42px; color: var(--grey-heading); }
  .tagline__main { font-size: 18.5px; font-weight: 500; letter-spacing: 0.2px; line-height: 1.1; }
  .tagline__sub { font-size: 10.5px; font-weight: 500; letter-spacing: 0.2px; margin-top: 3px; }

  .cover-panel { position: absolute; left: 169px; width: 882px; overflow: hidden; }
  .cover-panel--front { top: 150px; height: 356px; }
  .cover-panel--back { top: 698px; height: 358px; }

  .photo { position: absolute; inset: 0; }
  .photo--city {
    background: linear-gradient(180deg, #5d6f9a 0%, #9aa6c6 20%, #b6bfd6 30%, #3b4766 36%, #2d3550 55%, #3a3f52 75%, #24262e 100%);
  }
  .photo--glass {
    background: linear-gradient(125deg, #25b6ea 0%, #7ccbea 30%, #bfe6f4 50%, #4d9ab3 70%, #1d5a72 85%, #cbe9f5 100%);
  }

  .accent-strip { position: absolute; background: var(--brand-blue); opacity: 0.85; }
  .accent-strip--front-left { left: 0; top: 60px; width: 30px; height: 234px; }
  .accent-strip--back-right { left: 861px; top: 59px; width: 21px; height: 239px; opacity: 1; }

  .headline-block {
    position: absolute; left: 656px; top: 60px; width: 226px; height: 296px;
    background: var(--brand-blue-deep); opacity: 0.82;
  }
  .headline {
    position: absolute; left: 686px; top: 148px; color: var(--white);
  }
  .headline__main { font-size: 19.5px; font-weight: 500; line-height: 1; }
  .headline__sub { font-size: 11px; font-weight: 500; margin-top: 4px; }

  .edition { position: absolute; left: 198px; top: 586px; font-size: 18px; font-weight: 400; color: var(--grey-light); letter-spacing: 0.2px; }

  .wordmark { position: absolute; font-size: 21px; font-weight: 600; color: var(--ink); display: flex; align-items: center; gap: 8px; }
  .wordmark__square { width: 12px; height: 12px; background: var(--brand-cyan); }
  .wordmark--front { left: 860px; top: 578px; }
  .wordmark--back { left: 870px; top: 1130px; }

  .contact-block {
    position: absolute; left: 0; top: 59px; width: 526px; height: 239px;
    background: var(--brand-blue);
  }
  .contact {
    position: absolute; left: 76px; top: 105px; color: var(--white);
    font-size: 12.2px; line-height: 16px; font-weight: 400;
  }
  .contact__name { font-weight: 600; margin-bottom: 16px; }
  .contact__group + .contact__group { margin-top: 16px; }
</style>
</head>
<body>
  <header class="tagline">
    <div class="tagline__main">PREMIUM AERIAL MEDIA SOLUTIONS</div>
    <div class="tagline__sub">UNMANNED AERIAL VEHICLES</div>
  </header>

  <section class="cover-panel cover-panel--front">
    <div class="photo photo--city" role="img" aria-label="Aerial photograph of a sprawling city skyline at dusk with a tall tower on the right"></div>
    <div class="accent-strip accent-strip--front-left"></div>
    <div class="headline-block"></div>
    <div class="headline">
      <div class="headline__main">LET US CAPTURE</div>
      <div class="headline__sub">your vision</div>
    </div>
  </section>

  <div class="edition">CORPORATE BUSINESS BROCHURE 2016</div>
  <div class="wordmark wordmark--front"><span class="wordmark__square"></span>Tallow Merrin</div>

  <section class="cover-panel cover-panel--back">
    <div class="photo photo--glass" role="img" aria-label="Upward view of angular glass skyscrapers against a bright blue sky"></div>
    <div class="contact-block"></div>
    <div class="accent-strip accent-strip--back-right"></div>
    <address class="contact" style="font-style:normal">
      <div class="contact__name">TALLOW MERRIN</div>
      <div class="contact__group">
        <div>Tallow Merrin Pty Ltd.</div>
        <div>BRINDLE, WA 6099</div>
      </div>
      <div class="contact__group">
        <div>Telephone: 040 555 0182</div>
        <div>Fax: 040 555 0182</div>
        <div>contact@tallowmerrin.com.au</div>
      </div>
    </address>
  </section>

  <div class="wordmark wordmark--back"><span class="wordmark__square"></span>Tallow Merrin</div>
</body>
</html>
```